Bellmoor Commercial Finance Information Brochure

This brochure will be sent out to clients via A4 PDF on an email to showcase what our company has to offer. We are a commercial finance brokerage, that specialises in property finance. We would like to see designs following our colour scheme. The final design should demonstrate our professionalism and reliability.
I have attached our logo and also a few bullet points on our information and what we can offer. These can be slightly reworded for conciseness. Or leave the text sections as filler and I can fill these in.
I have also attached an overview of our colour scheme and design styling for your consideration.
Target Market(s)
Property Developers
Industry/Entity Type
Financial Services

```html
<!DOCTYPE html>
<html lang="en">
<head>
<meta charset="utf-8">
<title>Bellmoor Finance – Information Brochure</title>
<link href="https://fonts.googleapis.com/css2?family=Roboto+Condensed:wght@300;400;700&display=swap" rel="stylesheet">
<style>
  :root{
    --backdrop:#7fa98a;
    --paper:#ffffff;
    --brand-blue:#2340a0;
    --brand-green:#2a8a3e;
    --brand-teal:#0c80bf;
    --ink:#1d1d1d;
    --sky-light:#e8f5fa;
    --sky-mid:#9fd6e8;
    --sky-deep:#46b3cf;
  }
  *{margin:0;padding:0;box-sizing:border-box}
  html,body{width:1200px;height:898px;overflow:hidden}
  body{background:var(--backdrop);font-family:"Roboto Condensed",Arial,sans-serif;color:var(--ink)}
  .page{position:absolute;left:319px;top:50px;width:562px;height:798px;background:var(--paper);overflow:hidden;box-shadow:0 6px 18px rgba(0,0,0,.25)}
  .hero-photo{position:absolute;left:0;top:0;width:562px;height:300px;
    background:linear-gradient(100deg,#f4f7fa 0%,#dfeef5 35%,var(--sky-mid) 62%,var(--sky-deep) 100%)}
  .brand-name{position:absolute;left:350px;top:26px;width:200px;text-align:center;font-weight:700;font-size:22px;letter-spacing:1px;color:var(--brand-blue)}
  .hero-waves{position:absolute;left:0;top:220px}
  .headline{position:absolute;left:0;color:#fff;font-weight:700;font-size:22px;line-height:1;padding-left:14px;display:flex;align-items:center}
  .headline--question{top:220px;width:254px;height:37px;background:var(--brand-blue)}
  .headline--answer{top:257px;width:373px;height:43px;background:var(--brand-green)}
  .copy{position:absolute;font-weight:300;font-size:10px;line-height:13.1px;text-align:justify}
  .copy b{font-weight:700}
  .copy p+p{margin-top:8.5px}
  .copy--intro{left:15px;top:318px;width:531px}
  .copy--side{left:210px;top:415px;width:336px}
  .copy--wide{left:11px;top:525px;width:540px}
  .copy--closing{left:13px;top:612px;width:536px}
  .service{position:absolute;left:16px;width:179px;height:24px;border-radius:12px;color:#fff;font-weight:700;font-size:11px;display:flex;align-items:center;justify-content:center}
  .service--bridge{top:417px;background:var(--brand-blue)}
  .service--development{top:452px;background:var(--brand-green)}
  .service--btl{top:487px;background:var(--brand-teal)}
  .contact-prompt{position:absolute;left:16px;top:682px;font-size:10.5px;font-weight:400;color:var(--brand-blue);border-bottom:1px solid var(--brand-green);padding-bottom:1px}
  .footer-band{position:absolute;left:0;top:680px}
  .get-in-touch{position:absolute;left:24px;top:724px;width:82px;height:17px;border-radius:9px;background:var(--brand-green);color:#fff;font-size:10px;font-weight:700;display:flex;align-items:center;justify-content:center}
  .contact{position:absolute;color:#fff;font-size:10px;font-weight:700;display:flex;align-items:center;gap:4px;white-space:nowrap}
  .contact svg{flex:none}
  .contact--address{left:113px;top:746px}
  .contact--phones{left:113px;top:763px}
  .contact--email{left:326px;top:745px}
  .contact--web{left:326px;top:762px}
</style>
</head>
<body>
<main class="page">
  <div class="hero-photo" role="img" aria-label="Photo collage: business handshake over desk with charts and laptop, blending into construction site with cranes under a blue sky"></div>
  <div class="brand-name">BELLMOOR FINANCE</div>

  <svg class="hero-waves" width="562" height="120" viewBox="0 0 562 120" aria-hidden="true">
    <path d="M370 45 C430 10 500 0 562 10 L562 37 C500 25 430 30 370 60 Z" fill="var(--brand-green)"/>
    <path d="M370 60 C430 30 500 25 562 37 L562 112 C520 80 450 75 370 92 Z" fill="var(--brand-blue)"/>
    <path d="M370 92 C450 75 520 80 562 112 L562 120 L370 120 Z" fill="#fff"/>
  </svg>

  <h1 class="headline headline--question">WHAT SETS US APART?</h1>
  <h2 class="headline headline--answer">WELL, WE'VE WALKED IN YOUR SHOES.</h2>

  <div class="copy copy--intro">
    <p>As former lenders and developers ourselves, we intimately understand the inefficiencies that plague deals in the market today. We’ve experienced the frustration of tight time limits on deals and the exasperating feeling of brokers wasting precious time collecting information. <b>It’s enough to drive developers and lenders insane!</b></p>
    <p><b>That’s why we founded Bellmoor Finance – to be the efficient and reliable link that connects developers and lenders.</b> We’ve streamlined our processes to eliminate unnecessary hurdles, enabling clear and swift communication between all parties involved. <b>No more wasted time. No more unnecessary stress.</b></p>
  </div>

  <div class="service service--bridge">BRIDGE LOANS</div>
  <div class="service service--development">DEVELOPMENT FINANCE</div>
  <div class="service service--btl">BUY-TO-LET MORTGAGES</div>

  <div class="copy copy--side">
    <p>With our expertise and industry insights, we’ve developed a unique approach that simplifies the financing journey. <b>From the initial consultation to the final funding, we’re here to guide you every step of the way. Our goal? To make commercial financing a smooth and enjoyable experience for you.</b></p>
    <p>With our background in the asset management industry, <b>we have cultivated a black book of fund managers, institutions, UHNWI and private equity lenders that we can call on for non-traditional lending.</b></p>
  </div>

  <div class="copy copy--wide">
    <p><b>Bellmoor Finance was created to satisfy a need in the market that has been far too overlooked. Efficiency.</b> Efficiency is at the heart of our operations, and we pride ourselves on our ability to secure the best financing options swiftly and effectively for our clients. By employing cutting-edge technology and streamlining our internal processes, we have cultivated a seamless and time-saving approach to finance brokering. <b>Having been a developer, we understand the stresses and headaches associated with building, let alone all the paperwork and emails backwards and forwards between yourself and brokers to attain the necessary financing.</b></p>
  </div>

  <div class="copy copy--closing">
    <p>We are well-versed in the questions lenders will ask, allowing us to get ahead of the curve and request all the necessary information from you on day one. <b>This approach provides you with a distinct advantage, as it eliminates the need to allocate hours each day to answering questions and fulfilling requests from brokers. By entrusting us with this responsibility, you can focus on your core tasks and leave the financing aspect to us, making the process less stressful for you.</b></p>
  </div>

  <p class="contact-prompt">If you would like information about any of our services, please contact us.</p>

  <svg class="footer-band" width="562" height="118" viewBox="0 0 562 118" aria-hidden="true">
    <path d="M120 40 C300 30 460 15 562 0 L562 12 C460 25 300 36 120 40 Z" fill="var(--brand-green)"/>
    <path d="M0 40 C200 48 420 35 562 18 L562 118 L0 118 Z" fill="var(--brand-blue)"/>
  </svg>

  <div class="get-in-touch">GET IN TOUCH</div>

  <div class="contact contact--address">
    <svg width="8" height="10" viewBox="0 0 8 10"><path d="M4 0a3.5 3.5 0 0 0-3.5 3.5C.5 6 4 10 4 10s3.5-4 3.5-6.5A3.5 3.5 0 0 0 4 0zm0 5a1.5 1.5 0 1 1 0-3 1.5 1.5 0 0 1 0 3z" fill="#fff"/></svg>
    14 Harrowgate Row, Leeds LS2 8QT
  </div>
  <div class="contact contact--phones">
    <svg width="10" height="9" viewBox="0 0 10 9"><path d="M2 0.5l1.6 2-1 1c.6 1.3 1.6 2.3 2.9 2.9l1-1 2 1.6-.9 1.5C4.2 8.3 1.2 5.3.5 1.4z" fill="#fff"/></svg>
    0113-496-0182
    <svg width="12" height="10" viewBox="0 0 12 10"><rect x="4" y="0.5" width="5" height="9" rx="1" fill="none" stroke="#fff" stroke-width="1.2"/></svg>
    0113-496-0917
  </div>
  <div class="contact contact--email">
    <svg width="10" height="8" viewBox="0 0 10 8"><rect x=".5" y=".5" width="9" height="7" fill="none" stroke="#fff"/><path d="M.5 .5 5 4.5 9.5 .5" fill="none" stroke="#fff"/></svg>
    info@bellmoorfinance.com
  </div>
  <div class="contact contact--web">
    <svg width="10" height="10" viewBox="0 0 10 10"><circle cx="5" cy="5" r="4.3" fill="none" stroke="#fff" stroke-width="1.2"/><path d="M.7 5h8.6M5 .7c-2 2.5-2 6.1 0 8.6M5 .7c2 2.5 2 6.1 0 8.6" fill="none" stroke="#fff" stroke-width=".8"/></svg>
    www.bellmoorfinance.com
  </div>
</main>
</body>
</html>
```